Wordpress Identity for Innovation Firm

Lumen Harbor Partners is an innovation and investment firm based in Los Angeles.

We are seeking a designer that can help create our company identity and Wordpress site.

The attached Design Brief provides more details.

Designers Responsibility:

1) Company Identity

The designer will create the company identity.
Attached is a file that contains a type font that I like a lot.
No logo design is required.

The Lumen Harbor Partners type font should become the company identity.
The attached document provides an overview of company type font identities that we like.

2) Wordpress Theme & Design

The designer will select existing Wordpress Themes that meet our design desires, and present them as part of the design proposal.

We will make our selection based on the selected Wordpress Theme(s), which the designer will creatively adapt with the new company identity.

Target Market(s)

We anticipate the website being mostly accessed by the US, Canada and European countries.

Our target audience includes the following:

• Corporations, companies, startups, non-profits
• Banks, venture capital, private equity, investors
• Incubators, accelerators, innovation clusters, research labs, universities
• Ad agencies, marketing agencies, digital agencies, media, press

Industry/Entity Type

Investment

Number of Pages Required

1 page

Font styles to use
Sans Serif
Other font styles liked:
• See attached design brief materials. The Font will represent the brand identity!

Requirements
Must have
• The ability to scroll through information top to bottom is important to us.
• This is in line with today's Wordpress themes.
• The website must be able to function across devices (desktop, tablet, phone).
• The top 5 web browsers and platforms (Mac/PC/Android/iOS)
• Contact us link or information field
Nice to have
• It would be nice to have a moving image in the background, such as:
• https://tidalshowcase.examplesite.com
• The Wordpress theme of the moving image or video should be relevant to our overall Technology Innovation theme.
• Key words:
• Technology Innovation
• Digital
• Business
• Transportation
• Advanced Vehicles (auto, boat, airplane, rail, space)
• Space
• Venture Capital
• Investing
Should not have
• eCommerce

```html
<!DOCTYPE html>
<html lang="en">
<head>
<meta charset="utf-8">
<title>Lumen Harbor Partners</title>
<link href="https://fonts.googleapis.com/css2?family=Titillium+Web:ital,wght@0,300;0,400;0,600;0,700;1,400&display=swap" rel="stylesheet">
<style>
:root{
  --indigo:#2f2b9e;
  --indigo-dark:#27238a;
  --maroon:#6e1d50;
  --grey-bg:#efeeef;
  --line:#6a6a6a;
  --text:#444;
  --muted:#777;
  --white:#fff;
  --ink:#1c1c1c;
}
*{margin:0;padding:0;box-sizing:border-box}
html,body{width:1200px;height:3936px;overflow:hidden}
body{position:relative;font-family:"Titillium Web",Arial,sans-serif;color:var(--text);background:var(--white)}
.abs{position:absolute}
.center{text-align:center;left:0;width:1200px}

/* nav */
.site-nav{top:0;left:0;width:1200px;height:48px;background:var(--white)}
.brand{left:60px;top:12px;font-weight:700;font-size:17px;color:var(--ink);letter-spacing:.5px}
.menu{right:60px;top:14px;display:flex;gap:62px;font-size:14px;color:var(--ink)}

/* hero */
.hero{top:48px;left:0;width:1200px;height:664px;
  background:linear-gradient(100deg,rgba(120,90,220,.45) 0%,rgba(0,0,0,0) 22%,rgba(0,0,0,0) 78%,rgba(90,150,230,.45) 100%),
  linear-gradient(180deg,#5a5a5e 0%,#9a9a9c 45%,#4a4a4e 100%)}
.hero-title{top:318px;font-size:42px;font-weight:300;color:var(--white);letter-spacing:1px}
.hero-sub{top:410px;font-size:21px;font-weight:300;color:var(--white);line-height:30px}
.hero-btn{top:548px;left:531px;width:138px;height:38px;background:var(--white);color:var(--ink);font-size:13px;font-weight:700;letter-spacing:1px;line-height:38px;text-align:center}

/* registration */
.registration{top:712px;left:0;width:1200px;height:268px;background:var(--indigo)}
.reg-title{top:758px;font-size:24px;color:var(--white);letter-spacing:1px}
.reg-sub{top:794px;font-size:15px;color:#c9c7f0}
.field{top:864px;width:270px;height:40px;border-bottom:1px solid #9c99e0;color:#b9b6ee;font-size:12px;padding-top:10px;padding-left:20px}
.signup{top:872px;left:1004px;width:120px;height:34px;background:var(--white);color:var(--indigo);font-size:12px;font-weight:700;line-height:34px;text-align:center;letter-spacing:1px}

/* mission */
.mission{top:980px;left:0;width:1200px;height:860px;background:var(--grey-bg)}
.world-map{top:1110px;left:80px;width:1040px;height:700px;background:radial-gradient(ellipse at center,#dcdbdd 0%,#e8e7e9 60%,var(--grey-bg) 100%)}
.section-title{font-size:24px;color:#333;letter-spacing:.5px}
.timeline-line{top:1180px;left:598px;width:4px;height:580px;background:var(--line)}
.timeline-dot{left:584px;width:32px;height:32px;border-radius:50%;background:var(--line)}
.mission-card{width:250px;height:120px;background:var(--maroon);color:var(--white);font-size:15px;line-height:20px;padding:20px 40px 0 34px}
.card-left{clip-path:polygon(0 0,86% 0,100% 50%,86% 100%,0 100%)}
.card-right{clip-path:polygon(14% 0,100% 0,100% 100%,14% 100%,0 50%);padding-left:56px;padding-right:18px}
.step-num{font-size:86px;font-weight:700;color:var(--maroon);line-height:1}

/* bring */
.pattern{background:linear-gradient(135deg,#6fd0e8 0%,#9a7be0 40%,#e77ec9 75%,rgba(255,255,255,0) 100%)}
.bring-sub{top:2090px;font-size:16px;font-weight:600;font-style:italic;color:var(--indigo)}
.bring-text{top:2140px;left:260px;width:680px;text-align:center;font-size:14px;line-height:28px;color:var(--text)}
.quote{top:2300px;left:380px;width:440px;text-align:center;font-size:14px;font-style:italic;line-height:22px;color:var(--muted)}
.quote-mark{font-size:80px;font-weight:700;color:var(--ink);line-height:1}
.divider{top:2460px;left:300px;width:600px;height:1px;background:#ccc}

/* team */
.member{top:2680px;width:300px;text-align:center}
.portrait{margin:0 auto;width:240px;height:240px;position:relative}
.portrait .frame{position:absolute;left:36px;top:36px;width:168px;height:168px;transform:rotate(45deg);border:2px solid #999;background:linear-gradient(180deg,#d6d6d6,#8d8d8d)}
.member-name{margin-top:116px;font-size:18px;color:#333;letter-spacing:.5px}
.member-role,.member-phone{font-size:13px;color:var(--muted);line-height:20px}
.member-desc{margin-top:14px;font-size:13px;color:var(--muted);line-height:20px}

/* map */
.map{top:3280px;left:0;width:1200px;height:380px;background:linear-gradient(160deg,#d8d2c4 0%,#cdd0c6 45%,#9fc0c9 80%,#8ab3c2 100%)}
.pin{top:3460px;left:744px}

/* footer */
.footer{top:3660px;left:0;width:1200px;height:276px;background:var(--indigo-dark)}
.f-brand{top:3712px;left:60px;font-weight:700;font-size:17px;color:var(--white)}
.social{top:3754px;left:60px;display:flex;gap:14px}
.social span{width:14px;height:14px;border-radius:50%;background:var(--white);display:block}
.copyright{top:3878px;left:60px;font-size:11px;color:#b9b6ee}
.f-head{top:3712px;font-size:15px;color:var(--white);letter-spacing:.5px}
.f-text{font-size:12px;line-height:20px;color:#c9c7f0}
.news-input{top:3856px;left:490px;width:150px;height:30px;border:1px solid #8a87d6;font-size:11px;color:#b9b6ee;padding:6px 10px}
.news-btn{top:3856px;left:640px;width:80px;height:30px;background:#e6e5f5;color:var(--indigo);font-size:11px;line-height:30px;text-align:center}
</style>
</head>
<body>

<header class="abs site-nav">
  <div class="abs brand">LUMEN HARBOR</div>
  <nav class="abs menu"><span>Products</span><span>Solution</span><span>About</span><span>Blog</span><span>Contact</span></nav>
</header>

<section class="abs hero" role="img" aria-label="Team meeting in a glass office, with colourful geometric tiles along both sides"></section>
<h1 class="abs center hero-title">LUMEN HARBOR PARTNERS</h1>
<p class="abs center hero-sub">A Systems Innovation and<br>Growth Investment Firm</p>
<div class="abs hero-btn">LEARN MORE</div>

<section class="abs registration"></section>
<h2 class="abs center reg-title">REGISTRATION</h2>
<p class="abs center reg-sub">Signup in few clicks and start discover open space with us</p>
<div class="abs field" style="left:76px">Name</div>
<div class="abs field" style="left:376px">Email</div>
<div class="abs field" style="left:676px">Phone</div>
<div class="abs signup">SIGNUP</div>

<section class="abs mission"></section>
<div class="abs world-map" role="img" aria-label="Faint dotted world map"></div>
<h2 class="abs center section-title" style="top:1052px">OUR MISSION</h2>
<div class="abs timeline-line"></div>
<div class="abs timeline-dot" style="top:1164px"></div>
<div class="abs timeline-dot" style="top:1344px"></div>
<div class="abs timeline-dot" style="top:1584px"></div>
<div class="abs timeline-dot" style="top:1744px"></div>

<div class="abs step-num" style="left:214px;top:1136px">1</div>
<div class="abs mission-card card-left" style="left:290px;top:1120px">Create sustainable competitive advantage through superior innovation</div>

<div class="abs step-num" style="left:956px;top:1316px">2</div>
<div class="abs mission-card card-right" style="left:668px;top:1300px">Create sustainable competitive advantage through superior innovation</div>

<div class="abs step-num" style="left:214px;top:1556px">3</div>
<div class="abs mission-card card-left" style="left:290px;top:1540px">Operating performance and thus the ability to provide de-risked partnership models</div>

<div class="abs step-num" style="left:956px;top:1716px">4</div>
<div class="abs mission-card card-right" style="left:668px;top:1700px">Operating performance and thus the ability to provide de-risked partnership models</div>

<div class="abs pattern" style="top:1840px;left:0;width:220px;height:460px" role="img" aria-label="Colourful diamond tile pattern"></div>
<div class="abs pattern" style="top:1840px;left:980px;width:220px;height:460px;transform:scaleX(-1)" role="img" aria-label="Colourful diamond tile pattern"></div>
<h2 class="abs center section-title" style="top:2044px">WHAT WE BRING TO THE TABLE</h2>
<p class="abs center bring-sub">We build new Business</p>
<p class="abs bring-text">Today's age of innovation is driven by the accelerating evolution of technology and data, which has fundamentally changed consumer behavior. As a result, companies are faced with unrelenting pressure to put innovation at the center of their business. Lumen Harbor Partners builds startups for our partners, while focusing on their strategic transformation. We invest intellectual capital and funds, thus sharing entrepreneurial risk through success-based partnership strategies.</p>

<div class="abs quote-mark" style="left:360px;top:2284px">&ldquo;</div>
<p class="abs quote">Clear thinking, steady capital and patient teams turn bold ideas into lasting ventures. We stand beside founders from the first sketch to the first market, and we stay for the long road that follows every launch.</p>
<div class="abs quote-mark" style="left:812px;top:2384px">&rdquo;</div>
<div class="abs divider"></div>

<h2 class="abs center section-title" style="top:2532px">OUR AMAZING TEAM</h2>
<div class="abs member" style="left:95px">
  <div class="portrait"><div class="frame" role="img" aria-label="Portrait photo of a team member"></div></div>
  <div class="member-name">OWEN REYES</div>
  <div class="member-role">Creative Director</div>
  <div class="member-phone">+1 (555) 0142 386</div>
  <div class="member-desc">Conveniently revolt adaptive and<br>effective solutions rather than<br>premium e-markets.</div>
</div>
<div class="abs member" style="left:450px">
  <div class="portrait"><div class="frame" role="img" aria-label="Portrait photo of a team member"></div></div>
  <div class="member-name">LENA PARK</div>
  <div class="member-role">Creative Director</div>
  <div class="member-phone">+1 (555) 0142 387</div>
  <div class="member-desc">Conveniently revolt adaptive and<br>effective solutions rather than<br>premium e-markets.</div>
</div>
<div class="abs member" style="left:805px">
  <div class="portrait"><div class="frame" role="img" aria-label="Portrait photo of a team member"></div></div>
  <div class="member-name">MARCUS HALE</div>
  <div class="member-role">Creative Director</div>
  <div class="member-phone">+1 (555) 0142 388</div>
  <div class="member-desc">Conveniently revolt adaptive and<br>effective solutions rather than<br>premium e-markets.</div>
</div>

<div class="abs map" role="img" aria-label="Street map of the office area by the coast"></div>
<svg class="abs pin" width="32" height="46" viewBox="0 0 32 46" aria-hidden="true">
  <path d="M16 0C7 0 0 7 0 16c0 12 16 30 16 30s16-18 16-30C32 7 25 0 16 0z" fill="#6e1d50"/>
  <circle cx="16" cy="16" r="6" fill="#fff"/>
</svg>

<footer class="abs footer"></footer>
<div class="abs f-brand">LUMEN HARBOR</div>
<div class="abs social"><span></span><span></span><span></span></div>
<div class="abs copyright">&copy; 2017 Lumen Harbor. All rights reserved</div>

<div class="abs f-head" style="left:490px">NEWSLETTER</div>
<p class="abs f-text" style="top:3746px;left:490px;width:230px">Subscribe today to our briefing for news and insights on new ventures, sent once a month.</p>
<div class="abs news-input">Email</div>
<div class="abs news-btn">JOIN</div>

<div class="abs f-head" style="left:900px">CONTACTS</div>
<p class="abs f-text" style="top:3752px;left:900px;width:260px">214 Harbor Lane, Los Angeles, CA 90012<br>Phone: +1 (555) 010-2234<br>Fax: +1 (555) 010-2235<br>Email: hello@lumenharbor.example<br>Website: www.lumenharbor.example</p>

</body>
</html>
```